New Business Cards for Organic Meat Farm

We need a business card designed for Thornbury Farm, a meat farm in western MA. Our logo uses a hand-drawn woodcut (attached). Our color palette has been simply black and white (shown in notepad and picture of our food truck). While we are based out of western MA, we have ambitions to grow nationally, so our hope is for a classy and memorable card which will be printed on a premium quality stock from a printer like printkestrel.com.
Target Market(s)
consumers of quality meats, restauranteurs, partnering farms
Industry/Entity Type
Farming and prepared meat products
Contact Information for Business Card
Wendell Pruitt, President/Owner, wendell@thornburyfarm.com, mobile: 413-555-0172, phone: 413-555-0148, thornburyfarm.com, facebook: @thornburyfarm, instagram: @thornburyfarmma
Colors
Designer to choose colors to be used in the design.
Look and feel

```html
<!DOCTYPE html>
<html lang="en">
<head>
<meta charset="utf-8">
<title>Thornbury Farm – Business Card</title>
<link href="https://fonts.googleapis.com/css2?family=Josefin+Sans:wght@400;600&family=Lobster&display=swap" rel="stylesheet">
<style>
  :root {
    --backdrop: #9a9a9a;
    --card-dark: #232323;
    --emboss-text: #4a4a4a;
    --emboss-art: #1b1b1b;
    --card-light: #ffffff;
    --ink: #111111;
    --ghost-art: #f2f2f2;
  }
  * { margin: 0; padding: 0; box-sizing: border-box; }
  html, body { width: 1200px; height: 1000px; overflow: hidden; }
  body { background: var(--backdrop); position: relative; font-family: "Josefin Sans", sans-serif; color: var(--ink); }

  .card { position: absolute; left: 253px; width: 694px; height: 400px; border-radius: 18px; overflow: hidden; }
  .card--front { top: 68px; background: var(--card-dark); }
  .card--back { top: 525px; background: var(--card-light); }

  .front-illustration {
    position: absolute; left: 180px; top: 68px; width: 308px; height: 135px;
    background: linear-gradient(180deg, #1e1e1e, var(--emboss-art));
    border-radius: 6px;
  }
  .front-wordmark {
    position: absolute; left: 0; right: 0; top: 222px; text-align: center;
    font-family: "Josefin Sans", sans-serif; font-weight: 600;
    font-size: 44px; letter-spacing: 2px; color: var(--emboss-text);
  }

  .back-illustration {
    position: absolute; left: 197px; top: 0; width: 497px; height: 215px;
    background: linear-gradient(90deg, rgba(242,242,242,0) 0%, var(--ghost-art) 25%, var(--ghost-art) 100%);
  }

  .holder-name {
    position: absolute; left: 84px; top: 106px;
    font-family: "Lobster", cursive; font-weight: 400; font-size: 36px; color: var(--ink);
  }
  .holder-title {
    position: absolute; left: 89px; top: 160px;
    font-size: 11px; letter-spacing: 1.6px; color: #222;
  }

  .contact-list { position: absolute; left: 89px; top: 211px; list-style: none; }
  .contact-list li { display: flex; align-items: center; height: 21.6px; font-size: 15.5px; letter-spacing: 0.3px; }
  .contact-list svg { width: 15px; height: 15px; margin-right: 12px; flex: none; }

  .badge {
    position: absolute; left: 461px; top: 183px; width: 166px; height: 166px;
    border: 2.5px solid var(--ink); border-radius: 50%; background: var(--card-light);
    display: flex; flex-direction: column; align-items: center; justify-content: center;
  }
  .badge-illustration {
    width: 112px; height: 52px; margin-top: -10px;
    background: linear-gradient(180deg, #6a6a6a, #2a2a2a); border-radius: 4px;
  }
  .badge-wordmark {
    margin-top: 14px; font-weight: 600; font-size: 16px; letter-spacing: 0.3px; color: var(--ink);
    white-space: nowrap;
  }
</style>
</head>
<body>

<section class="card card--front" aria-label="Card front">
  <div class="front-illustration" role="img" aria-label="Embossed woodcut of the farmhouse among trees"></div>
  <div class="front-wordmark">Thornbury Farm</div>
</section>

<section class="card card--back" aria-label="Card back">
  <div class="back-illustration" role="img" aria-label="Faint woodcut of the farmhouse and trees"></div>

  <h1 class="holder-name">Wendell Pruitt</h1>
  <p class="holder-title">PRESIDENT/OWNER</p>

  <ul class="contact-list">
    <li>
      <svg viewBox="0 0 16 16" aria-hidden="true"><rect x="1" y="3.5" width="14" height="9" fill="#111"/><path d="M1.5 4 L8 9 L14.5 4" stroke="#fff" stroke-width="1.2" fill="none"/></svg>
      wendell@thornburyfarm.com
    </li>
    <li>
      <svg viewBox="0 0 16 16" aria-hidden="true"><rect x="4" y="1" width="8" height="14" rx="1.5" fill="none" stroke="#111" stroke-width="1.8"/><rect x="7" y="12" width="2" height="1.2" fill="#111"/></svg>
      413-555-0172
    </li>
    <li>
      <svg viewBox="0 0 16 16" aria-hidden="true"><path d="M3 2 L6 2 L7 5.5 L5.3 6.8 C6.2 8.8 7.4 10 9.3 10.8 L10.6 9.1 L14 10.1 L14 13.2 C14 14 13.3 14.5 12.5 14.4 C7 13.7 2.4 9.1 1.7 3.6 C1.6 2.7 2.2 2 3 2 Z" fill="#111"/></svg>
      413-555-0148
    </li>
    <li>
      <svg viewBox="0 0 16 16" aria-hidden="true"><circle cx="8" cy="8" r="6.5" fill="none" stroke="#111" stroke-width="1.4"/><ellipse cx="8" cy="8" rx="2.8" ry="6.5" fill="none" stroke="#111" stroke-width="1.2"/><path d="M1.5 8 H14.5 M2.5 5 H13.5 M2.5 11 H13.5" stroke="#111" stroke-width="1"/></svg>
      thornburyfarm.com
    </li>
    <li>
      <svg viewBox="0 0 16 16" aria-hidden="true"><circle cx="8" cy="8" r="7" fill="#111"/></svg>
      @thornburyfarm
    </li>
    <li>
      <svg viewBox="0 0 16 16" aria-hidden="true"><circle cx="8" cy="8" r="7" fill="#111"/></svg>
      @thornburyfarmma
    </li>
  </ul>

  <div class="badge">
    <div class="badge-illustration" role="img" aria-label="Woodcut of the farmhouse"></div>
    <div class="badge-wordmark">Thornbury Farm</div>
  </div>
</section>

</body>
</html>
```